Verodex business card

Business card for sustainable investment company called "Verodex". Verodex is an exchange platform selling carbon credits between buyers and sellers. Carbon Credits are an environmental commodity for reducing global carbon emissions.

the card should obviously have our logo and the theme should be sustainability/environment mixed with a trading platform.

Contact Information for Business Card

Logo, Name, Title, Phone, Email

Colors
0054AA
0677BA
7BADD7
CADEEF
E8F1F8
0094D4
00A9DD
6FCCEA
C7EBF8
E9F6FB
00AB8E
00BBA5
67D7C9
C6EFE9
E9F9F6
59FF00
82FF00
B8FF75
E3FFCB
F4FFEA

```html
<!DOCTYPE html>
<html lang="en">
<head>
<meta charset="utf-8">
<title>Verodex Business Card</title>
<link rel="stylesheet" href="https://fonts.googleapis.com/css2?family=Montserrat:wght@600;700&family=Mulish:wght@400;600&display=swap">
<style>
  :root {
    --navy: #1b2d5a;
    --navy-deep: #13214a;
    --ink: #1d2f55;
    --sky: #3cc0ea;
    --ocean: #0677ba;
    --paper: #ffffff;
    --stage: #e6e9ee;
    --muted: #2a2f3a;
  }
  * { margin: 0; padding: 0; box-sizing: border-box; }
  html, body { width: 1200px; height: 960px; overflow: hidden; }
  body {
    background: var(--stage);
    display: flex;
    flex-direction: column;
    align-items: center;
    justify-content: center;
    gap: 40px;
    font-family: "Mulish", Arial, sans-serif;
  }
  .card {
    width: 700px;
    height: 400px;
    border-radius: 28px;
    position: relative;
    box-shadow: 0 10px 30px rgba(20, 30, 60, 0.18);
    overflow: hidden;
  }
  .card--front {
    background: linear-gradient(135deg, #213a6c 0%, var(--navy) 45%, var(--navy-deep) 100%);
    display: flex;
    align-items: center;
    justify-content: center;
  }
  .brand {
    display: flex;
    align-items: center;
    gap: 22px;
  }
  .brand__dot {
    border-radius: 50%;
    background: linear-gradient(135deg, var(--sky), var(--ocean));
  }
  .brand__name {
    font-family: "Montserrat", Arial, sans-serif;
    font-weight: 600;
    letter-spacing: 0.02em;
  }
  .card--front .brand__dot { width: 78px; height: 78px; }
  .card--front .brand__name { color: var(--paper); font-size: 66px; }

  .card--back { background: var(--paper); }
  .card--back .brand {
    position: absolute;
    left: 52px;
    top: 52px;
    gap: 16px;
  }
  .card--back .brand__dot { width: 46px; height: 46px; }
  .card--back .brand__name { color: var(--ink); font-size: 38px; }

  .person {
    position: absolute;
    right: 56px;
    top: 150px;
    text-align: right;
  }
  .person__name {
    font-family: "Montserrat", Arial, sans-serif;
    font-weight: 700;
    font-size: 27px;
    color: var(--ink);
    letter-spacing: 0.01em;
  }
  .person__name .surname { color: var(--sky); }
  .person__title {
    font-size: 19px;
    color: var(--muted);
    margin-top: 2px;
  }

  .contact {
    position: absolute;
    left: 60px;
    bottom: 42px;
    list-style: none;
    display: flex;
    flex-direction: column;
    gap: 6px;
  }
  .contact__item {
    display: flex;
    align-items: center;
    gap: 12px;
    font-size: 19px;
    color: var(--muted);
  }
  .contact__icon { width: 20px; height: 20px; flex: none; }
</style>
</head>
<body>
  <section class="card card--front" aria-label="Card front">
    <div class="brand">
      <span class="brand__dot"></span>
      <span class="brand__name">VERODEX</span>
    </div>
  </section>

  <section class="card card--back" aria-label="Card back">
    <div class="brand">
      <span class="brand__dot"></span>
      <span class="brand__name">VERODEX</span>
    </div>

    <div class="person">
      <p class="person__name">DANIEL <span class="surname">HARTWELL</span></p>
      <p class="person__title">Co-Founder</p>
    </div>

    <ul class="contact">
      <li class="contact__item">
        <svg class="contact__icon" viewBox="0 0 24 24" aria-hidden="true">
          <path fill="#0094D4" d="M6.6 10.8a15.1 15.1 0 0 0 6.6 6.6l2.2-2.2a1 1 0 0 1 1-.25 11.4 11.4 0 0 0 3.6.57 1 1 0 0 1 1 1V20a1 1 0 0 1-1 1A17 17 0 0 1 3 4a1 1 0 0 1 1-1h3.5a1 1 0 0 1 1 1c0 1.25.2 2.45.57 3.57a1 1 0 0 1-.25 1z"/>
        </svg>
        555-014-2273
      </li>
      <li class="contact__item">
        <svg class="contact__icon" viewBox="0 0 24 24" aria-hidden="true">
          <rect x="2" y="5" width="20" height="14" rx="2" fill="#0094D4"/>
          <path d="M3 6l9 7 9-7" fill="none" stroke="#fff" stroke-width="1.6"/>
        </svg>
        info@verodex.com
      </li>
      <li class="contact__item">
        <svg class="contact__icon" viewBox="0 0 24 24" aria-hidden="true">
          <circle cx="12" cy="12" r="10" fill="#0094D4"/>
          <path d="M2 12h20M12 2c3 3 3 17 0 20M12 2c-3 3-3 17 0 20" fill="none" stroke="#fff" stroke-width="1.3"/>
        </svg>
        www.verodex.com
      </li>
    </ul>
  </section>
</body>
</html>
```